First of a series of workplace posters- our values statement

To produce a high quality poster of our values, we would like one in a3 and one in a4 both full colour
By utilising the supplied text , the intent is to produce a really striking poster for all our work places, which set out our company values. we are looking for really strong graphical elements which support the message visually . This will be the first of a series of posters, so we are looking to establish at stylistic theme for all with this one. for more on our business,

Target Market(s)

Internal and external audiences, our clients are all tier one companies

Requirements
Must have
• contemporary design rather than conservative, visually striking
• Must be clearly readable from a reasonable distance
Nice to have
• would be nice to tie in to the blue and greens of our logo in similar fashion to our website. www.kbtgreenworks.com
Should not have
• Difficult to read fonts,

```html
<!DOCTYPE html>
<html lang="en">
<head>
<meta charset="UTF-8">
<title>Values Poster 02 – All our workplaces are safe</title>
<link rel="stylesheet" href="https://fonts.googleapis.com/css2?family=Montserrat:wght@400;500;700;800&display=swap">
<style>
  :root {
    --green-deep: #0c2f19;
    --green-dark: #123d22;
    --green-mid: #1f5a33;
    --green-light: #3d7a50;
    --white: #ffffff;
  }
  * { margin: 0; padding: 0; box-sizing: border-box; }
  html, body { width: 849px; height: 1200px; overflow: hidden; background: var(--green-deep); }
  .poster {
    position: relative;
    width: 849px;
    height: 1200px;
    overflow: hidden;
    background: var(--green-deep);
    font-family: "Montserrat", Arial, sans-serif;
    color: var(--white);
  }
  .hero-photo {
    position: absolute;
    left: 0; top: 0;
    width: 849px; height: 900px;
    background:
      radial-gradient(ellipse 420px 260px at 560px 700px, rgba(90,140,100,0.55), transparent 70%),
      radial-gradient(ellipse 300px 500px at 120px 300px, rgba(10,35,18,0.9), transparent 75%),
      linear-gradient(160deg, var(--green-dark) 0%, var(--green-mid) 45%, var(--green-light) 62%, var(--green-dark) 85%, var(--green-deep) 100%);
  }
  .hero-fade {
    position: absolute;
    left: 0; top: 620px;
    width: 849px; height: 300px;
    background: linear-gradient(180deg, rgba(12,47,25,0) 0%, var(--green-deep) 95%);
  }
  .headline {
    position: absolute;
    left: 84px; top: 104px;
    font-size: 64px;
    font-weight: 800;
    line-height: 66px;
    letter-spacing: -0.5px;
  }
  .poster-number {
    position: absolute;
    right: 92px; top: 108px;
    font-size: 104px;
    font-weight: 700;
    line-height: 1;
    letter-spacing: 2px;
  }
  .intro {
    position: absolute;
    left: 84px; top: 362px;
    width: 410px;
    font-size: 15px;
    line-height: 20px;
    font-weight: 400;
  }
  .intro p + p { margin-top: 18px; }
  .commitments-title {
    position: absolute;
    left: 84px; top: 720px;
    font-size: 38px;
    font-weight: 700;
  }
  .commitments {
    position: absolute;
    left: 84px; top: 818px;
    width: 690px;
    list-style: none;
    font-size: 20px;
    line-height: 25px;
    font-weight: 500;
  }
  .commitments li {
    position: relative;
    padding-left: 30px;
    margin-bottom: 12px;
  }
  .commitments li::before {
    content: "";
    position: absolute;
    left: 6px; top: 10px;
    width: 7px; height: 7px;
    border-radius: 50%;
    background: var(--white);
  }
  .tagline {
    position: absolute;
    right: 94px; top: 1098px;
    font-size: 19px;
    font-weight: 700;
  }
</style>
</head>
<body>
  <main class="poster">
    <div class="hero-photo" role="img" aria-label="Green-tinted photograph of two business people in suits shaking hands"></div>
    <div class="hero-fade"></div>

    <h1 class="headline">All our<br>workplaces<br>are safe.</h1>
    <div class="poster-number">02</div>

    <div class="intro">
      <p>There is nothing more important to us than our team members going home healthy and safe every day, we won't accept anything less.</p>
      <p>We believe workplace safety is a management choice, by providing safe work systems and education we achieve our daily goal of Zero Harm.</p>
    </div>

    <h2 class="commitments-title">We:</h2>
    <ul class="commitments">
      <li>Take the time to make our work areas safe, whatever it takes.</li>
      <li>Don't accept shortcuts.</li>
      <li>Look out for each other.</li>
      <li>Investigate our incidents and learn from them, no repeats.</li>
      <li>Are constantly looking for ways to improve the safety of our workplaces and the health of our team members.</li>
    </ul>

    <p class="tagline">Think safe, works safe, go home safe!</p>
  </main>
</body>
</html>
```